Therapy Games Business Needs a Flyer for Conference Bag

Kindle Paths is an on-line business which provides resources and training for professionals who provide therapy to children and adolescents. I am putting a flyer into a conference bag and would like to let the conference attendees know about our resources which are all available online. The conference is called Bright Minds at Class and attendees would by psychologists, school counsellors, and staff associated with student well-being.
The main products I would like promoted are games on social skills and anger management - including -Grumpy Critters, Hint Tiles, Boiling Over or Cooling Off, Feelings Lotto (all can be viewed at www.kindlepaths.com.au).
The aim is to get them to the website to buy however signing up for the e-newsletter is very important.

Industry/Entity Type

Training

```html
<!DOCTYPE html>
<html lang="en">
<head>
<meta charset="utf-8">
<title>Kindle Paths – Flyer</title>
<link rel="stylesheet" href="https://fonts.googleapis.com/css2?family=Arimo:wght@400;700&display=swap">
<style>
  :root {
    --band-blue: #8ec3dc;
    --ink-grey: #505050;
    --logo-grey: #3f3f3f;
    --leaf-green: #7cc243;
    --white: #ffffff;
    --pat-orange: #f28a1e;
    --pat-magenta: #9c2a8a;
    --pat-blue: #1f6fb8;
    --pat-green: #6dbb45;
    --pat-yellow: #f7c21a;
    --pat-red: #e8432c;
  }
  * { margin: 0; padding: 0; box-sizing: border-box; }
  html, body { width: 846px; height: 1200px; overflow: hidden; background: #fff; }
  .flyer {
    position: relative;
    width: 846px;
    height: 1200px;
    overflow: hidden;
    font-family: "Arimo", Arial, sans-serif;
  }
  .pattern-backdrop {
    position: absolute; inset: 0;
    background: linear-gradient(135deg, var(--pat-orange) 0%, var(--pat-magenta) 22%, var(--pat-blue) 42%, var(--pat-green) 60%, var(--pat-yellow) 78%, var(--pat-red) 100%);
  }
  .logo-card {
    position: absolute;
    left: 26px; top: 42px;
    width: 320px; height: 184px;
    background: var(--white);
    border-radius: 20px;
    display: flex; align-items: center; justify-content: center;
    gap: 14px;
  }
  .logo-mark {
    width: 30px; height: 30px;
    background: var(--leaf-green);
  }
  .logo-name {
    font-size: 40px;
    font-weight: 400;
    color: var(--logo-grey);
  }
  .intro-band {
    position: absolute;
    left: 0; top: 270px;
    width: 846px; height: 346px;
    background: var(--band-blue);
    padding: 30px 30px 0 84px;
  }
  .intro-headline {
    color: var(--white);
    font-size: 37px;
    font-weight: 400;
    line-height: 43px;
    width: 720px;
  }
  .intro-copy {
    margin-top: 30px;
    color: var(--ink-grey);
    font-size: 21.5px;
    line-height: 28px;
    width: 715px;
  }
  .product-panel {
    position: absolute;
    left: 86px; top: 663px;
    width: 800px; height: 380px;
    background: var(--white);
    border-radius: 24px 0 0 24px;
  }
  .product-shot {
    position: absolute;
    width: 174px; height: 174px;
    border-radius: 16px;
    overflow: hidden;
  }
  .shot-art { position: absolute; inset: 0; }
  .shot-title {
    position: absolute;
    left: 8px; right: 8px;
    font-weight: 700;
    font-size: 17px;
    line-height: 19px;
    text-align: center;
  }
  .shot-critters { left: 108px; top: 714px; }
  .shot-critters .shot-art { background: linear-gradient(160deg, #3d8b3a, #6aae3e 55%, #8bc34a); }
  .shot-critters .shot-title { bottom: 34px; color: #f4c21e; font-size: 20px; }
  .shot-hints { left: 290px; top: 783px; }
  .shot-hints .shot-art { background: linear-gradient(160deg, #e04a3a 0%, #f2f2f2 35%, #4aa3d8 62%, #c9a888 100%); }
  .shot-hints .shot-title { top: 74px; color: #ffffff; }
  .shot-boiling { left: 468px; top: 714px; }
  .shot-boiling .shot-art { background: linear-gradient(160deg, #f28a3a, #e9813a 30%, #4a9fd8 60%, #3d8fc9); }
  .shot-boiling .shot-title { top: 8px; color: #1e3c7a; font-size: 16px; }
  .shot-lotto { left: 649px; top: 801px; }
  .shot-lotto .shot-art { background: linear-gradient(160deg, #f6f6f6 0%, #f8e06a 45%, #f08ab8 75%, #8ecfee 100%); }
  .shot-lotto .shot-title { top: 18px; color: #3a8a3a; font-size: 19px; }
  .site-url {
    position: absolute;
    right: 30px; top: 1086px;
    color: var(--white);
    font-size: 52px;
    line-height: 60px;
    font-weight: 400;
    letter-spacing: -0.5px;
  }
</style>
</head>
<body>
<main class="flyer">
  <div class="pattern-backdrop" role="img" aria-label="Colourful geometric cube pattern in orange, purple, blue, green, yellow and red"></div>

  <div class="logo-card">
    <span class="logo-mark"></span>
    <span class="logo-name">Kindle Paths</span>
  </div>

  <section class="intro-band">
    <h1 class="intro-headline">If you are working with children and adolescents, you know that sometimes the smallest change can result in the biggest breakthrough...</h1>
    <p class="intro-copy">Our wealth of resources includes books, games and puzzles that may assist with a range of problems, from separation and divorce to depression and behaviour management</p>
  </section>

  <div class="product-panel"></div>

  <figure class="product-shot shot-critters">
    <div class="shot-art" role="img" aria-label="Photo of the Grumpy Critters anger management board game"></div>
    <figcaption class="shot-title">Grumpy Critters</figcaption>
  </figure>
  <figure class="product-shot shot-hints">
    <div class="shot-art" role="img" aria-label="Photo of Hint Tiles cards with a question spinner"></div>
    <figcaption class="shot-title">Hint Tiles</figcaption>
  </figure>
  <figure class="product-shot shot-boiling">
    <div class="shot-art" role="img" aria-label="Photo of the Boiling Over or Cooling Off game board"></div>
    <figcaption class="shot-title">Boiling Over or Cooling Off</figcaption>
  </figure>
  <figure class="product-shot shot-lotto">
    <div class="shot-art" role="img" aria-label="Photo of the Feelings Lotto matching game box"></div>
    <figcaption class="shot-title">Feelings Lotto</figcaption>
  </figure>

  <p class="site-url">www.kindlepaths.com.au</p>
</main>
</body>
</html>
```